Retail Seafood business needs package/label design

In need of packaging/label design for multiple seafood products such as sword fish, halibut, cod fish, scallops, mahi, catfish, and lobster tails

```html
<!DOCTYPE html>
<html lang="en">
<head>
<meta charset="utf-8">
<title>Tidewell Market – Lobster Tails Carton</title>
<link rel="stylesheet" href="https://fonts.googleapis.com/css2?family=Libre+Baskerville:ital,wght@1,700&family=Playfair+Display:ital,wght@1,700&family=Oswald:wght@400;500;600&display=swap">
<style>
  :root {
    --ocean-blue: #1f5ea8;
    --deep-blue: #184f91;
    --paper-white: #ecedef;
    --magenta: #c8127a;
    --magenta-dark: #8f0f5d;
    --lobster-grey: #a9abae;
    --side-text: #c9ccd3;
    --backdrop: #dcdcde;
  }
  * { box-sizing: border-box; margin: 0; padding: 0; }
  html, body {
    width: 1200px; height: 1200px; overflow: hidden;
    background: var(--backdrop);
  }
  .panel {
    position: absolute; left: 60px;
    background: var(--ocean-blue);
    overflow: hidden;
  }

  /* ---------- top face ---------- */
  .lid { top: 60px; width: 1080px; height: 620px; }
  .lid-shape { position: absolute; inset: 0; width: 100%; height: 100%; }
  .product-line {
    position: absolute; right: 60px; top: 24px;
    font-family: "Libre Baskerville", "Times New Roman", serif;
    font-style: italic; font-weight: 700;
    font-size: 38px; letter-spacing: 3px;
    color: #ffffff;
  }
  .brand-title {
    position: absolute; left: 200px; top: 86px;
    font-family: "Playfair Display", Georgia, serif;
    font-style: italic; font-weight: 700;
    font-size: 54px; line-height: 1;
    color: var(--magenta);
  }
  .brand-mark {
    position: absolute; left: 60px; top: 268px;
    display: flex; align-items: center; gap: 14px;
  }
  .brand-mark .dot {
    width: 30px; height: 30px; border-radius: 50%;
    background: var(--magenta);
  }
  .brand-mark .name {
    font-family: "Oswald", Arial, sans-serif; font-weight: 600;
    font-size: 48px; letter-spacing: 2px; line-height: 1.2;
    color: var(--magenta);
  }
  .net-weight, .storage-note {
    position: absolute;
    font-family: "Oswald", Arial, sans-serif; font-weight: 600;
    font-size: 24px; letter-spacing: 1px;
    color: var(--magenta);
  }
  .net-weight { left: 60px; top: 345px; }
  .storage-note { right: 60px; bottom: 30px; }
  .lobster-art {
    position: absolute; left: 420px; top: 240px;
    width: 440px; height: 290px;
    border-radius: 48% 42% 46% 40%;
    background: radial-gradient(ellipse at center, #c3c5c8 0%, var(--lobster-grey) 55%, rgba(169,171,174,0.25) 100%);
  }
  .cert-badge {
    position: absolute; right: 60px; top: 250px;
    width: 130px; height: 110px;
    background: var(--deep-blue);
    border-radius: 6px;
  }

  /* ---------- long side panel ---------- */
  .side-front {
    top: 680px; width: 1080px; height: 170px;
    border-top: 2px solid var(--deep-blue);
  }
  .side-front .row {
    position: absolute; inset: 0;
    display: flex; align-items: center; justify-content: space-between;
    padding: 0 60px;
    transform: rotate(180deg);
  }
  .side-text {
    font-family: "Oswald", Arial, sans-serif; font-weight: 500;
    font-size: 26px; letter-spacing: 1px;
    color: var(--side-text);
  }
  .side-front .brand-mark { position: static; }

  /* ---------- short end panel ---------- */
  .side-end {
    top: 870px; width: 620px; height: 170px;
    display: flex; align-items: center; justify-content: space-between;
    padding: 0 40px;
  }
  .end-line {
    font-family: "Oswald", Arial, sans-serif; font-weight: 400;
    font-size: 30px; color: var(--side-text);
  }
  .end-brand {
    font-family: "Playfair Display", Georgia, serif;
    font-style: italic; font-weight: 700;
    font-size: 36px; line-height: 1.05; text-align: center;
    color: var(--magenta);
  }
</style>
</head>
<body>
  <main class="panel lid">
    <svg class="lid-shape" viewBox="0 0 1080 620" preserveAspectRatio="none" aria-hidden="true">
      <path d="M0 250 C 300 180, 700 185, 1080 210 L1080 620 L0 620 Z" fill="var(--paper-white)"/>
      <path d="M0 250 C 300 180, 700 185, 1080 210 L1080 195 C 700 165, 300 158, 0 225 Z" fill="var(--magenta)"/>
      <path d="M0 225 C 300 158, 700 165, 1080 195 L1080 188 C 700 157, 300 150, 0 216 Z" fill="var(--magenta-dark)"/>
    </svg>

    <p class="product-line">Premium Quality Lobster Tails</p>
    <h1 class="brand-title">Tidewell Market</h1>

    <div class="brand-mark">
      <span class="dot"></span>
      <span class="name">Tidewell</span>
    </div>
    <p class="net-weight">NET WT. 16 OZ. (1LB.) 454G.</p>

    <div class="lobster-art" role="img" aria-label="Grey line illustration of a lobster"></div>
    <div class="cert-badge" role="img" aria-label="Sustainable seafood certification badge"></div>

    <p class="storage-note">KEEP FROZEN&nbsp;&nbsp;DO NOT REFREEZE</p>
  </main>

  <section class="panel side-front" aria-label="Long side panel">
    <div class="row">
      <p class="side-text">NET WT. 16 OZ. (1LB.) 454G.</p>
      <div class="brand-mark">
        <span class="dot"></span>
        <span class="name">Tidewell</span>
      </div>
      <p class="side-text">KEEP FROZEN&nbsp;&nbsp;DO NOT REFREEZE</p>
    </div>
  </section>

  <section class="panel side-end" aria-label="End panel">
    <p class="end-line">Premium Quality</p>
    <p class="end-brand">Tidewell<br>Market</p>
    <p class="end-line">Lobster Tails</p>
  </section>
</body>
</html>
```